Local Roofing/Construction company business needs new biz card design

We need a new business card design, current cards are from the start of this operation and generic at best. We are a local Construction Company (General Contractor) with a majority of our work originating from insurance claims-exterior finish work is the main focus (Roofs-Siding-Gutters etc). Heavily involved with homeowners and the low ball offers they receive from insurance company's after a insurable event takes place. I have attached some of our original logo file(s) below.

```html
<!DOCTYPE html>
<html lang="en">
<head>
<meta charset="utf-8">
<title>Ironvale Construction – Business Card</title>
<link href="https://fonts.googleapis.com/css2?family=Quicksand:wght@500;600;700&display=swap" rel="stylesheet">
<style>
  :root {
    --page-bg: #e9e6e1;
    --card-bg: #0c211f;
    --card-bg-light: #10302b;
    --brand-green: #4cbb6c;
    --text-light: #f2f5f3;
    --text-muted: #c9d4d0;
  }
  * { box-sizing: border-box; margin: 0; padding: 0; }
  html, body {
    width: 1200px; height: 900px; overflow: hidden;
    background: var(--page-bg);
    font-family: "Quicksand", sans-serif;
  }
  .stage { position: relative; width: 1200px; height: 900px; }
  .card {
    position: absolute; left: 320px; width: 560px; height: 320px;
    border-radius: 36px;
    background: linear-gradient(135deg, var(--card-bg) 0%, var(--card-bg-light) 100%);
    box-shadow: 0 10px 28px rgba(0,0,0,.28);
    color: var(--text-light);
    overflow: hidden;
  }
  .card--front { top: 80px; }
  .card--back  { top: 480px; }

  /* company name block */
  .brand { position: absolute; display: flex; align-items: center; gap: 12px; color: var(--brand-green); font-weight: 700; }
  .brand__square { width: 22px; height: 22px; background: var(--brand-green); flex: none; }
  .brand__name { line-height: 1.05; letter-spacing: .04em; text-transform: uppercase; }
  .card--front .brand { top: 34px; right: 38px; }
  .card--front .brand__name { font-size: 22px; }
  .card--back .brand { bottom: 38px; right: 38px; }
  .card--back .brand__name { font-size: 26px; }

  .heading { color: var(--brand-green); font-weight: 700; font-size: 15px; letter-spacing: .04em; text-transform: uppercase; margin-bottom: 6px; }

  .services { position: absolute; top: 40px; left: 40px; }
  .services__list { list-style: none; font-size: 14px; font-weight: 500; line-height: 1.55; }
  .services__list li { display: flex; align-items: center; gap: 8px; }
  .services__list svg { width: 12px; height: 12px; flex: none; }

  .connect { position: absolute; top: 150px; left: 40px; }
  .connect__hours { font-size: 14px; font-weight: 500; line-height: 1.5; }
  .connect__hours .label { color: var(--brand-green); }
  .connect__emergency { display: flex; align-items: center; gap: 8px; margin-top: 4px; font-size: 17px; font-weight: 600; }
  .connect__emergency .label { color: var(--brand-green); }
  .connect__emergency svg { width: 18px; height: 18px; }

  .rule { position: absolute; height: 1px; background: var(--brand-green); }
  .card--front .rule { left: 40px; right: 40px; bottom: 62px; }
  .tagline { position: absolute; bottom: 24px; left: 0; right: 0; text-align: center; font-weight: 700; font-size: 17px; letter-spacing: .02em; }

  .person { position: absolute; top: 118px; left: 40px; }
  .person__name { color: var(--brand-green); font-weight: 700; font-size: 20px; letter-spacing: .04em; text-transform: uppercase; }
  .person__role { font-size: 16px; font-weight: 500; margin-top: 2px; }

  .contact { position: absolute; top: 44px; left: 270px; list-style: none; font-size: 14px; font-weight: 500; line-height: 1.7; }
  .contact li { display: flex; align-items: flex-start; gap: 10px; }
  .contact svg { width: 15px; height: 15px; flex: none; margin-top: 4px; }
  .card--back .rule { left: 270px; right: 40px; top: 178px; }
</style>
</head>
<body>
<div class="stage">

  <section class="card card--front" aria-label="Business card front">
    <div class="brand">
      <span class="brand__square"></span>
      <span class="brand__name">Ironvale<br>Construction</span>
    </div>

    <div class="services">
      <h2 class="heading">Our Services</h2>
      <ul class="services__list">
        <li><svg viewBox="0 0 12 12"><path d="M2 6.5l2.5 2.5L10 3" fill="none" stroke="var(--brand-green)" stroke-width="2"/></svg>Residential Roofing</li>
        <li><svg viewBox="0 0 12 12"><path d="M2 6.5l2.5 2.5L10 3" fill="none" stroke="var(--brand-green)" stroke-width="2"/></svg>Commercial Roofing</li>
        <li><svg viewBox="0 0 12 12"><path d="M2 6.5l2.5 2.5L10 3" fill="none" stroke="var(--brand-green)" stroke-width="2"/></svg>Storm Restoration</li>
        <li><svg viewBox="0 0 12 12"><path d="M2 6.5l2.5 2.5L10 3" fill="none" stroke="var(--brand-green)" stroke-width="2"/></svg>Exterior Finishes</li>
      </ul>
    </div>

    <div class="connect">
      <h2 class="heading">Connect</h2>
      <p class="connect__hours"><span class="label">Monday - Friday:</span> 8am - 6pm</p>
      <p class="connect__hours"><span class="label">Saturday - Sunday:</span> By Appointment Only</p>
      <p class="connect__emergency">
        <svg viewBox="0 0 24 24"><path d="M6.6 10.8a15 15 0 006.6 6.6l2.2-2.2c.3-.3.7-.4 1-.2 1.1.4 2.3.6 3.6.6.6 0 1 .4 1 1V20c0 .6-.4 1-1 1A17 17 0 013 4c0-.6.4-1 1-1h3.5c.6 0 1 .4 1 1 0 1.3.2 2.5.6 3.6.1.3 0 .7-.2 1z" fill="var(--brand-green)"/></svg>
        <span class="label">Emergency:</span> 555-014-2290
      </p>
    </div>

    <div class="rule"></div>
    <p class="tagline">You Can Trust Our 30 Years Of Combined Experience</p>
  </section>

  <section class="card card--back" aria-label="Business card back">
    <div class="person">
      <h1 class="person__name">Dana Mercer</h1>
      <p class="person__role">Director</p>
    </div>

    <ul class="contact">
      <li><svg viewBox="0 0 24 24"><path d="M6.6 10.8a15 15 0 006.6 6.6l2.2-2.2c.3-.3.7-.4 1-.2 1.1.4 2.3.6 3.6.6.6 0 1 .4 1 1V20c0 .6-.4 1-1 1A17 17 0 013 4c0-.6.4-1 1-1h3.5c.6 0 1 .4 1 1 0 1.3.2 2.5.6 3.6.1.3 0 .7-.2 1z" fill="var(--brand-green)"/></svg>555-017-3381</li>
      <li><svg viewBox="0 0 24 24"><rect x="2" y="5" width="20" height="14" rx="1" fill="var(--brand-green)"/><path d="M2 6l10 7 10-7" fill="none" stroke="var(--card-bg)" stroke-width="1.6"/></svg>hello@ironvalebuild.com</li>
      <li><svg viewBox="0 0 24 24" fill="none" stroke="var(--brand-green)" stroke-width="1.8"><circle cx="12" cy="12" r="9.5"/><path d="M2.5 12h19M12 2.5c3 3 3 16 0 19M12 2.5c-3 3-3 16 0 19"/></svg>www.ironvalebuild.com</li>
      <li><svg viewBox="0 0 24 24"><path d="M12 2a7 7 0 00-7 7c0 5 7 13 7 13s7-8 7-13a7 7 0 00-7-7zm0 9.5A2.5 2.5 0 1112 6.5a2.5 2.5 0 010 5z" fill="var(--brand-green)"/></svg><span>48 Harlow Creek Rd<br>Maple Ridge, MO 63000</span></li>
    </ul>

    <div class="rule"></div>

    <div class="brand">
      <span class="brand__square"></span>
      <span class="brand__name">Ironvale<br>Construction</span>
    </div>
  </section>

</div>
</body>
</html>
```